Creative, fresh business card design for Orrin Linings

We need a fresh, creative business card design for Orrin Linings. We are the manufacturer of Orrin Linings in Australia. Wall panels are 2400 x 1200mm panels made from MDF and feature 3D patterns on the face of the panel. The colours to be used are green, silver/grey and white RGB
Red 187
Green 207
Blue 65.

An idea is to possibly use a watermark of one of our designs as a background (like on the "Ferns" design on the left hand side of page 2 of our brochure).

Target Market(s)

Interior designers, architects, builders and home renovators

Industry/Entity Type

Business

Contact Information for Business Card

Details to go on the card are:
Our logo (attached),
Slogan: "Decorative panels for interiors and exteriors",
Contact name,
Position,
Mobile phone number,
Business address,
Business phone,
Business fax,
Website and
Email address.

I have attached a few images of our panels and our brochure for reference.

The colours of the business card should feature our logo colours which are: RGB
Red 187
Green 207
Blue 65

Requirements
Must have
• Very modern fonts and design. Some of the designs shown especially the "Weave" design which is a popular design.
Nice to have
• Creative but simple design. Very contemporary.
Should not have
• Anything ornate or old fashioned.

```html
<!DOCTYPE html>
<html lang="en">
<head>
<meta charset="utf-8">
<title>Orrin Linings – Business Card</title>
<link rel="stylesheet" href="https://fonts.googleapis.com/css2?family=Open+Sans:wght@300;400;700&display=swap">
<style>
  :root {
    --brand-green: rgb(187, 207, 65);
    --brand-grey: #9a9b9d;
    --ink: #3a3b3d;
    --ink-soft: #6d6e70;
    --card-white: #f4f4f2;
    --card-shade: #e6e6e4;
    --stage: #e4e3df;
  }
  * { margin: 0; padding: 0; box-sizing: border-box; }
  html, body {
    width: 1200px; height: 1022px; overflow: hidden;
    background: var(--stage);
    font-family: "Open Sans", Arial, sans-serif;
  }
  .business-card {
    position: absolute; left: 100px; top: 226px;
    width: 1000px; height: 570px;
    box-shadow: 0 6px 24px rgba(0,0,0,0.18);
    overflow: hidden;
  }
  .panel-texture {
    position: absolute; inset: 0;
    background: radial-gradient(ellipse at 40% 40%, var(--card-white) 0%, var(--card-shade) 100%);
  }
  .edge-band {
    position: absolute; top: 0; right: 0; width: 46px; height: 100%;
    background: var(--brand-green);
  }
  .edge-band::before {
    content: ""; position: absolute; left: -10px; top: 0; width: 10px; height: 100%;
    background: #c9c9c9;
  }
  .divider {
    position: absolute; left: 300px; top: 332px; width: 610px; height: 2px;
    background: var(--brand-green);
  }
  .brand {
    position: absolute; left: 56px; top: 216px;
  }
  .brand-row { display: flex; align-items: center; gap: 12px; }
  .brand-square { width: 54px; height: 54px; background: var(--brand-green); }
  .brand-name { font-size: 30px; font-weight: 400; color: var(--brand-grey); letter-spacing: 0.5px; }
  .slogan {
    margin-top: 10px; width: 210px;
    font-size: 12.5px; font-weight: 300; color: var(--ink-soft);
    letter-spacing: 2px; line-height: 1.35;
  }
  .address {
    position: absolute; left: 312px; top: 252px;
    font-size: 27px; font-weight: 400; color: var(--ink); line-height: 1.35;
    letter-spacing: 0.5px;
  }
  .contact-list {
    position: absolute; left: 312px; top: 350px; list-style: none;
  }
  .contact-list li {
    display: flex; align-items: center; gap: 16px;
    font-size: 25px; color: var(--ink); line-height: 38px; letter-spacing: 0.5px;
  }
  .contact-list svg { width: 20px; height: 20px; flex: none; }
  .person {
    position: absolute; right: 90px; top: 246px; text-align: right;
  }
  .person-name { font-size: 36px; font-weight: 700; color: var(--brand-green); letter-spacing: 0.5px; line-height: 1.1; }
  .person-title { font-size: 24px; font-weight: 400; color: var(--ink); letter-spacing: 1px; margin-top: 2px; }
</style>
</head>
<body>
  <article class="business-card">
    <div class="panel-texture" role="img" aria-label="Faint embossed wall panel pattern across the card face"></div>
    <div class="edge-band"></div>
    <div class="divider"></div>

    <div class="brand">
      <div class="brand-row">
        <span class="brand-square"></span>
        <span class="brand-name">Orrin Linings</span>
      </div>
      <p class="slogan">decorative panels for interiors &amp; landscapes</p>
    </div>

    <p class="address">412 Carrow Lane<br>Brindlewood, NSW 2190</p>

    <ul class="contact-list">
      <li>
        <svg viewBox="0 0 20 20"><rect x="5" y="1" width="10" height="18" rx="2" fill="none" stroke="var(--brand-green)" stroke-width="2"/><circle cx="10" cy="15.5" r="1.2" fill="var(--brand-green)"/></svg>
        231. 480. 5127
      </li>
      <li>
        <svg viewBox="0 0 20 20"><path d="M4 2 L8 2 L9 6 L7 8 Q9 12 12 13 L14 11 L18 12 L18 16 Q17 18 14 18 Q4 16 2 5 Q2 2 4 2 Z" fill="var(--brand-green)"/></svg>
        437. 615. 2093
      </li>
      <li>
        <svg viewBox="0 0 20 20"><rect x="5" y="2" width="10" height="6" fill="var(--brand-green)"/><rect x="2" y="8" width="16" height="8" rx="1" fill="var(--brand-green)"/><rect x="5" y="13" width="10" height="5" fill="#fff" stroke="var(--brand-green)" stroke-width="1.5"/></svg>
        437. 615. 2094
      </li>
      <li>
        <svg viewBox="0 0 20 20"><rect x="1" y="4" width="18" height="12" fill="var(--brand-green)"/><path d="M1 4 L10 11 L19 4" fill="none" stroke="#fff" stroke-width="1.5"/></svg>
        leon@orrinlinings.com.au
      </li>
      <li>
        <svg viewBox="0 0 20 20"><circle cx="10" cy="10" r="8" fill="none" stroke="var(--brand-green)" stroke-width="2"/><ellipse cx="10" cy="10" rx="3.5" ry="8" fill="none" stroke="var(--brand-green)" stroke-width="1.5"/><path d="M2 10 H18" stroke="var(--brand-green)" stroke-width="1.5"/></svg>
        www.orrinlinings.com.au
      </li>
    </ul>

    <div class="person">
      <p class="person-name">Leon Harwick</p>
      <p class="person-title">President</p>
    </div>
  </article>
</body>
</html>
```